Clarinet Past Midnight: mini recital & soiree

I need a poster design for a recital I'm doing next Friday April 25. It's an "after party" from 10 - 1am where I'll be playing a 30 min program followed by a DJ and there'll be food wine etc. I want to see a very "sexy" kind of poster. Modern with a "south beach" kind of art deco feel but without the really cheesy connotation that south beach sometimes has (if that makes any sense). I've included the link for the Gatherlink event so you can get an idea of the feel I want.

Cheers!

https://www.gatherlink.example/events/519304762811095/

Target Market(s)

College Students at the Coral Ridge Institute

South Beach-ians

Industry/Entity Type

Events

Colors

Designer to choose colors to be used in the design.

Requirements
Must have
• Title of event..
Date..
Location..
Food / Beverage served..
DJ Torvik..

```html
<!DOCTYPE html>
<html lang="en">
<head>
<meta charset="utf-8">
<title>Clarinet Past Midnight – Poster</title>
<link rel="stylesheet" href="https://fonts.googleapis.com/css2?family=Oswald:wght@600&family=Montserrat:wght@300&family=Cabin:wght@600&display=swap">
<style>
  :root {
    --page: #ffffff;
    --night: #2a1b0b;
    --night-deep: #1b1106;
    --beam: #c9a640;
    --gold-light: #e9c878;
    --gold-mid: #b8893a;
    --gold-dark: #6e4c18;
    --wine-tone: #6a1a18;
    --ink-white: #ffffff;
  }
  * { margin: 0; padding: 0; box-sizing: border-box; }
  html, body {
    width: 900px; height: 1200px; overflow: hidden;
    background: var(--page);
  }
  .poster {
    position: absolute; left: 61px; top: 0;
    width: 778px; height: 1200px; overflow: hidden;
    background: radial-gradient(ellipse at 50% 55%, #3a2711 0%, var(--night) 45%, var(--night-deep) 100%);
  }
  .spotlights { position: absolute; inset: 0; width: 778px; height: 1200px; }
  .feature-photo {
    position: absolute; left: 400px; top: 610px; width: 378px; height: 590px;
    background:
      radial-gradient(ellipse 55% 40% at 38% 32%, rgba(106,26,24,0.75) 0%, rgba(106,26,24,0) 100%),
      radial-gradient(ellipse 90% 80% at 85% 40%, var(--gold-light) 0%, var(--gold-mid) 40%, var(--gold-dark) 75%, rgba(42,27,11,0) 100%);
  }
  .event-date {
    position: absolute; top: 138px; left: 0; width: 778px;
    text-align: center;
    font-family: "Oswald", sans-serif; font-weight: 600;
    font-size: 70px; line-height: 1; letter-spacing: -1.5px;
    color: var(--ink-white);
  }
  .event-title { position: absolute; left: 0; top: 230px; width: 778px; height: 400px; }
  .event-title text { font-family: "Montserrat", sans-serif; font-weight: 300; }
  .venue {
    position: absolute; left: 135px; top: 614px;
    font-family: "Cabin", sans-serif; font-weight: 600;
    font-size: 46px; line-height: 1; color: var(--ink-white);
  }
  .hours {
    position: absolute; left: 172px; top: 667px;
    font-family: "Cabin", sans-serif; font-weight: 600;
    font-size: 31px; line-height: 1; color: var(--ink-white);
  }
  .details {
    position: absolute; left: 46px; top: 910px;
    font-family: "Cabin", sans-serif; font-weight: 600;
    font-size: 47px; line-height: 56px; color: var(--ink-white);
  }
  .details .line-dj { padding-left: 16px; }
</style>
</head>
<body>
  <main class="poster">
    <svg class="spotlights" viewBox="0 0 778 1200" aria-hidden="true">
      <defs>
        <filter id="beam-soft" x="-20%" y="-20%" width="140%" height="140%">
          <feGaussianBlur stdDeviation="22"/>
        </filter>
        <radialGradient id="beam-glow" cx="50%" cy="50%" r="50%">
          <stop offset="0%" stop-color="#e8c860" stop-opacity="0.5"/>
          <stop offset="100%" stop-color="#e8c860" stop-opacity="0"/>
        </radialGradient>
      </defs>
      <g filter="url(#beam-soft)" fill="var(--beam)" opacity="0.5">
        <polygon points="-40,150 20,110 450,640 360,690"/>
        <polygon points="818,150 758,110 330,640 420,690"/>
      </g>
      <ellipse cx="390" cy="650" rx="190" ry="80" fill="url(#beam-glow)"/>
    </svg>

    <div class="feature-photo" role="img" aria-label="Photograph of a gold clarinet with a glass of red wine in front of it"></div>

    <h2 class="event-date">FRIDAY APRIL 25</h2>

    <svg class="event-title" viewBox="0 230 778 400" role="img" aria-label="Clarinet Past Midnight">
      <defs>
        <linearGradient id="title-gold" x1="0" y1="0" x2="0" y2="1">
          <stop offset="0%" stop-color="#f6e3a0"/>
          <stop offset="50%" stop-color="#d6ac4c"/>
          <stop offset="100%" stop-color="#9c7326"/>
        </linearGradient>
      </defs>
      <text x="134" y="303" font-size="90" textLength="516" lengthAdjust="spacingAndGlyphs" fill="url(#title-gold)">CLARINET</text>
      <text x="107" y="454" font-size="178" textLength="553" lengthAdjust="spacingAndGlyphs" fill="url(#title-gold)">PAST</text>
      <text x="110" y="606" font-size="178" textLength="520" lengthAdjust="spacingAndGlyphs" fill="url(#title-gold)">MIDNIGHT</text>
    </svg>

    <p class="venue">Harlow Hall Commons</p>
    <p class="hours">10:00 pm - 1:00am</p>

    <div class="details">
      <p class="line-dj">Music By: DJ Torvik</p>
      <p class="line-food">Food / Beverage served..</p>
    </div>
  </main>
</body>
</html>
```